Psychotherapy and emotion coaching with feloQuin requires web design

I need a web design for emotion coaching (release of emotional blockages) (psychotherapy) with the target group trauma-related disorders and anxiety disorders. The website should be clear and well-organized, i.e. rather simple. The colors should be light, blue, green and yellow are desirable. The design should radiate security.

A logo already exists and should be used appropriately.

Three columns should describe the following
-Emotion regulation
-Imaginative structure constellations
-Ego-State-Therapy

An outdated draft can be seen here:
www.klarer-mutweg.example
The website should advertise coded in Wordpress.

I need the landing page, for which there are drafts now, and at least one more page (maybe a template) for further information (like "About me")

Target Market(s)

Clients for coaching and therapy with trauma or axienty disorders;

Coding

Coded - Design and coding required

Number of Pages Required

3 page

Font styles to use
Sans Serif

Colors
0054AA
0677BA
7BADD7
CADEEF
E8F1F8
59FF00
82FF00
B8FF75
E3FFCB
F4FFEA
FFF300
FFF600
FEFA6F
FFFEC7
FFFEE8

Requirements
Nice to have
• Title: "More happiness and satisfaction in life"
Should not have
• "Therapy" should not be listed in the header; Instead "More happiness and satisfaction in life"

```html
<!DOCTYPE html>
<html lang="en">
<head>
<meta charset="utf-8">
<title>feloQuin – More happiness and satisfaction in life</title>
<link href="https://fonts.googleapis.com/css2?family=Montserrat:wght@400;500;600;700;800&family=Roboto:wght@400&display=swap" rel="stylesheet">
<style>
:root{
  --yellow:#fcc10e;
  --yellow-light:#ffd93a;
  --orange:#f5a623;
  --green:#44b649;
  --blue:#4f8df2;
  --blue-dark:#2a63d8;
  --ink:#1d1d1d;
  --line:#d9d9d9;
  --black:#111;
  --soft:#f3f7fb;
}
*{box-sizing:border-box;margin:0;padding:0}
html,body{width:1200px;height:2949px;overflow:hidden}
body{position:relative;font-family:"Montserrat",sans-serif;background:#fff;color:var(--ink)}
.abs{position:absolute}
.topline{left:0;top:0;width:1200px;height:4px;background:var(--green)}
.brand{left:145px;top:14px;display:flex;align-items:center;gap:16px}
.brand-dot{width:62px;height:62px;border-radius:50%;background:var(--yellow)}
.brand-name{font-size:28px;font-weight:500;color:#333}
.phone-top{right:176px;top:16px;display:flex;align-items:center;gap:8px;font-weight:700;font-size:19px}
.phone-badge{width:26px;height:28px;background:var(--yellow);border-radius:6px;display:flex;align-items:center;justify-content:center}
.lang{right:144px;top:24px;width:14px;height:10px;background:#34548f}
.nav{left:548px;top:65px;display:flex;font-size:13px;font-weight:500;color:#222}
.nav span{margin-right:28px}
.nav span:last-child{margin-right:0}
.hero{left:0;top:90px;width:1200px;height:640px}
.hero-hex{left:118px;top:110px;width:398px;height:456px}
.hero-copy{left:140px;top:228px;width:350px;text-align:center;color:#fff}
.hero-copy h1{font-size:44px;line-height:50px;font-weight:800}
.hero-copy p{font-size:30px;font-weight:600;margin-top:10px}
.btn{display:inline-flex;align-items:center;justify-content:center;color:#fff;font-weight:700;font-size:13px;border-radius:30px;text-transform:uppercase}
.btn-blue{background:linear-gradient(90deg,#6aa7ff,var(--blue-dark))}
.btn-green{background:linear-gradient(90deg,#5dc55a,#1f8a2a)}
.btn-yellow{background:linear-gradient(90deg,#ffd21f,var(--orange))}
.dots{left:1126px;top:320px;display:flex;flex-direction:column;gap:8px}
.dots i{width:8px;height:8px;border-radius:50%;background:#fff;display:block}
.dots i.on{background:var(--blue)}
.about-title{left:145px;top:770px;font-size:40px;font-weight:800;line-height:50px}
.about-title em{font-style:normal;font-weight:600;color:var(--yellow)}
.about-intro{left:147px;top:882px;width:432px;font-size:15px;line-height:25px;color:#666}
.about-list{left:147px;top:975px;width:410px;list-style:none;font-size:14px;line-height:24px;color:#333}
.about-list li{position:relative;padding-left:22px}
.about-list li::before{content:"";position:absolute;left:0;top:9px;width:7px;height:7px;border-radius:50%;background:var(--green)}
.about-panel{left:660px;top:760px;width:360px;height:420px;border-radius:24px;background:var(--soft)}
.portrait{left:700px;top:790px;width:280px;height:330px;border-radius:16px;background:linear-gradient(180deg,#3d6a3a,#a7b9cc)}
.services-bg{left:0;top:1230px;width:1200px;height:820px}
.services-title{left:0;top:1358px;width:1200px;text-align:center;font-size:40px;font-weight:800}
.card{position:absolute;top:1446px;width:296px;height:515px}
.card svg{position:absolute;left:0;top:0}
.card-body{position:absolute;left:20px;top:272px;width:256px;text-align:center}
.card h3{font-size:18px;font-weight:500;line-height:21px;color:#222}
.card p{font-size:12px;line-height:17px;color:#444;margin-top:10px}
.card .btn{position:absolute;left:88px;top:436px;width:119px;height:40px;font-size:11px}
.contact-bg{left:0;top:2026px;width:1200px;height:552px}
.contact-title{left:0;top:2080px;width:1200px;text-align:center;font-size:40px;font-weight:800}
.contact-intro{left:0;top:2145px;width:1200px;text-align:center;font-size:15px;color:#555}
.field{position:absolute;border:1px solid var(--line);background:#fff;font-family:"Roboto",sans-serif;font-size:16px;color:#555;padding:18px 22px}
.footer{left:0;top:2576px;width:1200px;height:373px;background:var(--black);color:#fff}
.f-item{position:absolute;display:flex;align-items:center;gap:20px;font-size:16px;line-height:28px}
.f-nav{position:absolute;left:0;top:160px;width:1200px;display:flex;justify-content:center;gap:40px;font-size:18px;font-weight:500}
.f-copy{position:absolute;left:0;top:214px;width:1200px;text-align:center;font-size:14px}
.f-social{position:absolute;left:530px;top:267px;display:flex;gap:9px}
.f-social i{width:42px;height:42px;border-radius:50%;border:2px solid #fff;display:block}
.f-social i.on{background:var(--green);border-color:var(--green)}
.chat{position:absolute;left:1071px;top:310px;width:32px;height:32px;border-radius:50%;background:var(--blue)}
.bottomline{position:absolute;left:0;top:367px;width:1200px;height:6px;background:var(--green)}
</style>
</head>
<body>

<div class="abs topline"></div>
<header>
  <div class="abs brand"><span class="brand-dot"></span><span class="brand-name">feloQuin</span></div>
  <div class="abs phone-top">
    <span class="phone-badge"><svg width="14" height="14" viewBox="0 0 24 24"><path fill="#fff" d="M6.6 10.8a15 15 0 0 0 6.6 6.6l2.2-2.2c.3-.3.7-.4 1-.2 1.1.4 2.3.6 3.6.6.6 0 1 .4 1 1V20c0 .6-.4 1-1 1A17 17 0 0 1 3 4c0-.6.4-1 1-1h3.5c.6 0 1 .4 1 1 0 1.3.2 2.5.6 3.6.1.3 0 .7-.2 1z"/></svg></span>
    0160 400 23 118
  </div>
  <div class="abs lang"></div>
  <nav class="abs nav"><span>START</span><span>JONAS</span><span>ABOUT EMDR</span><span>FELOQUIN®</span><span>OFFER</span><span>CONTACT</span></nav>
</header>

<section class="abs hero">
  <svg width="1200" height="640" viewBox="0 0 1200 640">
    <defs>
      <linearGradient id="sky" x1="0" y1="0" x2="0" y2="1">
        <stop offset="0" stop-color="#e8b98a"/><stop offset=".45" stop-color="#e5a865"/><stop offset="1" stop-color="#b0602e"/>
      </linearGradient>
    </defs>
    <path role="img" aria-label="Photo: woman in a white dress and hat raising her arms on a sunlit hill" fill="url(#sky)" d="M0 0H1200V430L596 610L0 430Z"/>
    <path fill="none" stroke="var(--green)" stroke-width="10" d="M0 440L596 610L1200 440"/>
    <path fill="none" stroke="var(--blue)" stroke-width="12" d="M0 456L596 626L1200 456"/>
  </svg>
  <div class="dots abs"><i></i><i class="on"></i><i></i></div>
</section>
<svg class="abs hero-hex" viewBox="0 0 398 456">
  <path fill="var(--yellow-light)" d="M199 0L398 112V344L199 456L0 344V112Z"/>
  <path fill="var(--yellow)" d="M199 24L376 124V332L199 432L22 332V124Z"/>
  <path fill="none" stroke="#fff" stroke-width="8" d="M22 332L199 432L376 332"/>
</svg>
<div class="abs hero-copy">
  <h1>LET GO OF<br>BURDENS!</h1>
  <p>Find more joy in life!</p>
</div>
<a class="btn btn-blue abs" style="left:238px;top:399px;width:157px;height:54px">Get started</a>

<section>
  <h2 class="abs about-title">JONAS BRENNER<br><em>(psychotherapist)</em></h2>
  <p class="abs about-intro">If you have just reached one of the following points in life, I would be happy to support you in finding ways out ofthe crisis and bring about change:</p>
  <ul class="abs about-list">
    <li>You or someone close to you has been diagnosed with a serious illness such as cancer(Psycho-oncology)·</li>
    <li>You suffer from fears, phobias or illnesses such as tinnitus·</li>
    <li>You have had bad or traumatic experiences and/or are suffering from their consequences or from post traumaticStress disorder</li>
    <li>You are having difficulties at work or with your partner</li>
    <li>You are in a crisis or situation of upheaval</li>
  </ul>
  <div class="abs about-panel"></div>
  <div class="abs portrait" role="img" aria-label="Portrait photo of the psychotherapist"></div>
</section>

<section>
  <svg class="abs services-bg" viewBox="0 0 1200 820">
    <path fill="var(--yellow)" d="M645 0L1200 155V690L900 800L780 820L0 700V185Z"/>
  </svg>
  <h2 class="abs services-title">MY SERVICES</h2>

  <article class="card" style="left:146px">
    <svg width="296" height="515" viewBox="0 0 296 515">
      <path fill="#fff" d="M0 0H296V420L148 515L0 420Z"/>
      <path role="img" aria-label="Photo: two children running through a summer meadow" fill="#a9c28a" d="M0 0H296V165L148 257L0 165Z"/>
    </svg>
    <div class="card-body">
      <h3>Emotion regulation through bifocal attention</h3>
      <p>Using this technique specifically those in the brain stored experiences block us, positivechanged. As a result, you win You lack self-confidence</p>
    </div>
    <a class="btn btn-yellow">Read more</a>
  </article>

  <article class="card" style="left:451px">
    <svg width="299" height="515" viewBox="0 0 299 515">
      <path fill="#fff" stroke="#6ecf7e" stroke-width="4" d="M2 2H297V420L150 513L2 420Z"/>
      <path role="img" aria-label="Photo: smiling couple standing together" fill="#9aa6b1" d="M6 6H293V165L150 257L6 165Z"/>
    </svg>
    <div class="card-body" style="left:22px">
      <h3>Imaginative structure constellations</h3>
      <p>We all have inherited ones Embossings and patterns that always conflicts cause or us slow down. In a lineup old patterns are revealed and changed</p>
    </div>
    <a class="btn btn-green" style="left:90px">Read more</a>
  </article>

  <article class="card" style="left:759px">
    <svg width="296" height="515" viewBox="0 0 296 515">
      <path fill="#fff" d="M0 0H296V420L148 515L0 420Z"/>
      <path role="img" aria-label="Illustration: colourful brain above many faces" fill="#b4786a" d="M0 0H296V165L148 257L0 165Z"/>
    </svg>
    <div class="card-body">
      <h3>Ego-State-Therapy</h3>
      <p>known as "ego-state coaching" or "Inner Team"). If criticism sometimes you have a feeling of Helplessness or inferiority triggers you sometimes back and forth feel torn or you have</p>
    </div>
    <a class="btn btn-blue">Read more</a>
  </article>
</section>

<section>
  <svg class="abs contact-bg" viewBox="0 0 1200 552">
    <path fill="none" stroke="var(--blue)" stroke-width="10" d="M0 520L150 475M1050 475L1200 520"/>
    <path fill="none" stroke="var(--green)" stroke-width="6" d="M0 532L150 488M1050 488L1200 532"/>
    <path fill="#fff" d="M175 0H1025L1160 278L1025 550H175L40 278Z"/>
  </svg>
  <h2 class="abs contact-title">GET IN TOUCH</h2>
  <p class="abs contact-intro">If you are interested in my offer or have any questions,Please feel free to call me or send me an email</p>
  <div class="field" style="left:233px;top:2198px;width:361px;height:55px">First Name</div>
  <div class="field" style="left:604px;top:2198px;width:361px;height:55px">Last Name</div>
  <div class="field" style="left:233px;top:2263px;width:361px;height:55px">Email address</div>
  <div class="field" style="left:604px;top:2263px;width:362px;height:55px">Phone Number</div>
  <div class="field" style="left:233px;top:2327px;width:733px;height:117px">Message</div>
  <a class="btn btn-blue abs" style="left:510px;top:2469px;width:180px;height:54px">Submit message</a>
</section>

<footer class="abs footer">
  <div class="f-item" style="left:184px;top:58px">
    <svg width="48" height="54" viewBox="0 0 48 54"><path fill="none" stroke="#fff" stroke-width="1.5" d="M24 1L47 14V40L24 53L1 40V14Z"/><path fill="#fff" d="M24 16a7 7 0 0 0-7 7c0 5 7 13 7 13s7-8 7-13a7 7 0 0 0-7-7zm0 10a3 3 0 1 1 0-6 3 3 0 0 1 0 6z"/></svg>
    <span>Jonas Brenner<br>Lindenweg 12 Musterstadt</span>
  </div>
  <div class="f-item" style="left:516px;top:60px">
    <svg width="48" height="54" viewBox="0 0 48 54"><path fill="var(--yellow)" d="M24 1L47 14V40L24 53L1 40V14Z"/><path fill="#fff" transform="translate(15 18) scale(.75)" d="M6.6 10.8a15 15 0 0 0 6.6 6.6l2.2-2.2c.3-.3.7-.4 1-.2 1.1.4 2.3.6 3.6.6.6 0 1 .4 1 1V20c0 .6-.4 1-1 1A17 17 0 0 1 3 4c0-.6.4-1 1-1h3.5c.6 0 1 .4 1 1 0 1.3.2 2.5.6 3.6.1.3 0 .7-.2 1z"/></svg>
    <span>0160 400 23 118</span>
  </div>
  <div class="f-item" style="left:754px;top:58px">
    <svg width="48" height="54" viewBox="0 0 48 54"><path fill="none" stroke="#fff" stroke-width="1.5" d="M24 1L47 14V40L24 53L1 40V14Z"/><rect x="14" y="19" width="20" height="15" rx="2" fill="#fff"/><path fill="none" stroke="#111" stroke-width="1.5" d="M14 20L24 28L34 20"/></svg>
    <span>kontakt@klarer-mutweg.example</span>
  </div>
  <nav class="f-nav"><span>START</span><span>JONAS</span><span>ABOUT EMDR</span><span>FELOQUIN®</span><span>OFFER</span><span>CONTACT</span></nav>
  <p class="f-copy">© 2024 feloQuin. All rights reserved.Privacy &nbsp;| &nbsp;Terms of Use</p>
  <div class="f-social"><i></i><i class="on"></i><i></i></div>
  <div class="chat"></div>
  <div class="bottomline"></div>
</footer>

</body>
</html>
```